New website for tarnholm.se using wordpress

- Tarnholm is a consultant broker based in Sweden
- Current web page: tarnholm.se
- We want a new web page and we are aiming for simple and "clean"
- Two target groups:
1. Consultants/Consultant firms looking for assignments
2. Clients looking for consultants
- Colors + Logo attached

Requirements
Must have
• The new site should have separate pages the different sections. We have to be able to link to each page separately. NOT like the current web page where all the content is on one page.

```html
<!DOCTYPE html>
<html lang="sv">
<head>
<meta charset="utf-8">
<title>Tarnholm – Konsultmäkleri</title>
<link rel="stylesheet" href="https://fonts.googleapis.com/css2?family=Lexend:wght@300;400;500;600&display=swap">
<style>
:root{
  --purple:#67329a;
  --black:#000000;
  --grey:#dcdcdc;
  --lavender:#f0eaf6;
  --soft:#f7f7f7;
  --muted:#8a8a8a;
  --backdrop:#efeef3;
}
*{margin:0;padding:0;box-sizing:border-box}
html,body{width:1200px;height:3188px;overflow:hidden}
body{position:relative;background:var(--backdrop);font-family:"Lexend",sans-serif;color:var(--black)}
.page{position:absolute;left:283px;top:277px;width:512px;height:2260px;background:#fff;transform:scale(1.238);transform-origin:0 0;overflow:hidden}
.page *{position:absolute}
.page :where(p,span,h1,h2,a){white-space:nowrap}
.logo{left:13px;top:9px;font-size:15px;font-weight:600;color:var(--purple);letter-spacing:-.3px}
.nav-link{top:15px;font-size:3.6px;color:var(--black)}
.nav-cta{left:454px;top:9px;width:46px;height:18px;background:var(--purple);color:#fff;font-size:3.4px;font-weight:600;display:flex;align-items:center;justify-content:center;letter-spacing:.3px}
.eyebrow{font-size:3.6px;letter-spacing:2.2px;color:var(--purple);text-transform:uppercase}
.hero-title{left:67px;top:80px;font-size:20.5px;font-weight:500;line-height:25px}
.hero-arrow{left:67px;top:150px}
.hero-links{left:421px;top:149px;font-size:3.4px;line-height:11px;color:var(--purple);text-decoration:underline}
.hero-links span{position:static;display:block}
.photo{background:linear-gradient(135deg,#e6e2de 0%,#cfc9c4 45%,#9c948e 100%)}
.hero-photo{left:0;top:197px;width:500px;height:236px}
.side-label{font-size:3.4px;letter-spacing:1.8px;text-transform:uppercase;color:var(--purple);transform:rotate(-90deg);transform-origin:0 0}
.sec-title{font-size:16px;font-weight:500;line-height:19.5px}
.sec-title .indent{position:static;display:block;padding-left:11px}
.sec-title .line{position:static;display:block}
.body-text{font-size:4px;line-height:10px;color:#555;white-space:normal}
.more{font-size:3.6px;display:flex;align-items:center;gap:4px}
.more svg{position:static}
.offer{left:13px;top:625px;width:487px;height:298px;background:var(--purple);color:#fff}
.offer .side-label{color:#d9c9ec}
.skill{width:70px;text-align:center;font-size:3.4px;color:#fff}
.skill svg{position:static;display:block;margin:0 auto 5px}
.form-label{font-size:3.4px;color:#333}
.field{width:93px;height:17px;background:#fff;border:.6px solid var(--grey)}
.send{left:252px;top:1119px;width:46px;height:18px;background:var(--purple);color:#fff;font-size:3.4px;font-weight:600;display:flex;align-items:center;justify-content:center}
.partners{left:13px;top:1176px;width:487px;height:190px;background:var(--soft)}
.badge{width:60px;height:11px;border-radius:2px;background:#dedede}
.quote-text{left:163px;top:1404px;width:225px;font-size:4px;line-height:8px;font-style:italic;font-weight:500;white-space:normal}
.quote-author{left:163px;top:1450px;font-size:3.2px;color:var(--muted)}
.jobs{left:8px;top:1492px;width:487px;height:196px;background:var(--lavender)}
.job{left:246px;width:193px;height:26px;border-bottom:.6px solid #cfc6d9}
.job-title{left:0;top:4px;font-size:4.2px}
.job-place{left:0;top:11px;font-size:2.8px;color:var(--muted);letter-spacing:.2px}
.job-arrow{right:4px;top:5px}
.jobs-photo{left:64px;top:1616px;width:106px;height:138px;background:linear-gradient(160deg,#eae7e3 0%,#c9c2b6 55%,#6f6a62 100%)}
.register{left:87px;top:1713px;width:61px;height:15px;background:var(--purple);color:#fff;font-size:3px;font-weight:600;display:flex;align-items:center;justify-content:center}
.person{width:96px;height:122px;background:var(--soft);text-align:center}
.person.active{background:var(--lavender)}
.avatar{left:28px;top:20px;width:40px;height:40px;border-radius:50%;border:.8px solid #bbb}
.avatar .fill{left:3px;top:3px;width:32px;height:32px;border-radius:50%;background:linear-gradient(160deg,#d8d2cc,#8f8780)}
.person-name{left:0;width:96px;top:73px;font-size:4px;font-weight:500}
.person-role{left:0;width:96px;top:81px;font-size:3px;color:var(--muted)}
.person-link{left:0;width:96px;top:90px;font-size:5px;font-weight:600;color:var(--purple)}
.news{left:13px;top:2029px;width:487px;height:191px;background:var(--soft)}
.news-item{left:151px;width:192px;height:24px;border-bottom:.6px solid var(--grey)}
.news-item p{left:0;top:0;font-size:4.2px}
.news-item svg{left:0;top:9px}
.footer-item{top:2234px;font-size:3.2px;color:#555;display:flex;align-items:center;gap:4px}
.footer-item svg{position:static}
</style>
</head>
<body>
<main class="page">
  <!-- Header -->
  <div class="logo">Tarnholm</div>
  <a class="nav-link" style="left:331px">Kund</a>
  <a class="nav-link" style="left:358px">Konsulter &amp; Partners</a>
  <a class="nav-link" style="left:419px">Om Tarnholm</a>
  <a class="nav-cta">KONTAKT</a>

  <!-- Hero -->
  <p class="eyebrow" style="left:67px;top:68px">Välkommen till Tarnholm</p>
  <h1 class="hero-title"><span style="position:static;display:block">Vi Forenklar Ert Inklov</span><span style="position:static;display:block">Inkop av Kompetens</span></h1>
  <svg class="hero-arrow" width="10" height="14" viewBox="0 0 10 14"><path d="M5 1v11M1 8l4 4 4-4" fill="none" stroke="var(--purple)" stroke-width=".8"/></svg>
  <div class="hero-links"><span>LÄS MER</span><span>AKTUELLA UPPDRAG</span><span>NYHETER</span></div>
  <div class="photo hero-photo" role="img" aria-label="Photo of three colleagues in a meeting at a table with laptops"></div>

  <!-- About -->
  <p class="side-label" style="left:68px;top:527px">Om Tarnholm</p>
  <h2 class="sec-title" style="left:91px;top:469px"><span class="indent">Söker Du</span><span class="line">Spetskompetyens?</span></h2>
  <p class="body-text" style="left:91px;top:523px;width:275px">Vi erbjuder ett komplett konsultmäkleri med personliga, enkla och etablerade processer som gör att vi snabbt kan hjälpa er med inköp av specialistkompetens. Tillsammans med vårt nätverk och vår anpassningsbara organisation kan vi leverera inom Ekonomi, HR och IT. Våra kunder finns över hela Sverige såväl inom den privata som den offentliga.</p>
  <div class="more" style="left:91px;top:579px">läs mer <svg width="7" height="7" viewBox="0 0 7 7"><circle cx="3.5" cy="3.5" r="3" fill="none" stroke="var(--purple)" stroke-width=".5"/><path d="M3 2l1.5 1.5L3 5" fill="none" stroke="var(--purple)" stroke-width=".5"/></svg></div>

  <!-- Competence areas -->
  <section class="offer">
    <p class="side-label" style="left:55px;top:92px">Vad vi erbjuder</p>
    <h2 class="sec-title" style="left:78px;top:36px"><span class="indent">Ett Axplock Av</span><span class="line">Våra Kompetensområden</span></h2>
    <div class="skill" style="left:66px;top:104px"><svg width="22" height="22" viewBox="0 0 22 22" fill="none" stroke="#fff" stroke-width=".8"><circle cx="10" cy="11" r="8"/><path d="M10 3v8h8"/></svg>Ekonomistyrning</div>
    <div class="skill" style="left:138px;top:104px"><svg width="22" height="22" viewBox="0 0 22 22" fill="none" stroke="#fff" stroke-width=".8"><rect x="3" y="2" width="12" height="18"/><path d="M6 6h6M6 10h6M6 14h3"/><circle cx="16" cy="15" r="4"/></svg>Redovisning</div>
    <div class="skill" style="left:211px;top:104px"><svg width="22" height="22" viewBox="0 0 22 22" fill="none" stroke="#fff" stroke-width=".8"><rect x="5" y="9" width="12" height="10" rx="2"/><path d="M8 9V6a3 3 0 016 0v3"/><circle cx="11" cy="14" r="1.5"/></svg>Controlling</div>
    <div class="skill" style="left:295px;top:104px"><svg width="22" height="22" viewBox="0 0 22 22" fill="none" stroke="#fff" stroke-width=".8"><rect x="4" y="2" width="13" height="17"/><circle cx="10" cy="9" r="3.5"/><path d="M12.5 11.5L18 18"/></svg>HR Business Partner</div>
    <div class="skill" style="left:375px;top:104px"><svg width="22" height="22" viewBox="0 0 22 22" fill="none" stroke="#fff" stroke-width=".8"><rect x="4" y="2" width="12" height="17"/><path d="M7 6h6M7 9h6"/><circle cx="16" cy="16" r="3.5"/><path d="M14.5 16l1 1 2-2"/></svg>HR Generalist</div>

    <div class="skill" style="left:66px;top:163px"><svg width="22" height="22" viewBox="0 0 22 22" fill="none" stroke="#fff" stroke-width=".8"><circle cx="11" cy="6" r="4"/><path d="M3 20c0-5 4-8 8-8s8 3 8 8"/></svg>Interim HR Manager</div>
    <div class="skill" style="left:138px;top:163px"><svg width="22" height="22" viewBox="0 0 22 22" fill="none" stroke="#fff" stroke-width=".8"><rect x="3" y="3" width="16" height="16"/><path d="M6 8h10M6 12h10M6 16h6"/></svg>Projektledning</div>
    <div class="skill" style="left:211px;top:163px"><svg width="22" height="22" viewBox="0 0 22 22" fill="none" stroke="#fff" stroke-width=".8"><rect x="2" y="10" width="12" height="9"/><circle cx="15" cy="7" r="5"/><path d="M5 16h6"/></svg>Business Intelligence</div>
    <div class="skill" style="left:295px;top:163px"><svg width="22" height="22" viewBox="0 0 22 22" fill="none" stroke="#fff" stroke-width=".8"><path d="M3 20V16M8 20V13M13 20V10M18 20V7M3 12L9 8l4 2 6-6"/></svg>Verksamhetsutveckling</div>
    <div class="skill" style="left:375px;top:163px"><svg width="22" height="22" viewBox="0 0 22 22" fill="none" stroke="#fff" stroke-width=".8"><path d="M11 3l8 4-8 4-8-4z M3 11l8 4 8-4 M3 15l8 4 8-4"/></svg>Systemutveckling</div>

    <div class="skill" style="left:66px;top:222px"><svg width="22" height="22" viewBox="0 0 22 22" fill="none" stroke="#fff" stroke-width=".8"><rect x="3" y="3" width="10" height="16"/><path d="M5 7h6M5 11h6M5 15h6"/><rect x="15" y="5" width="4" height="4"/><rect x="15" y="13" width="4" height="4"/></svg>Systemarkitektur</div>
    <div class="skill" style="left:138px;top:222px"><svg width="22" height="22" viewBox="0 0 22 22" fill="none" stroke="#fff" stroke-width=".8"><circle cx="6" cy="6" r="3"/><circle cx="16" cy="16" r="3"/><path d="M8 8l6 6M16 3v6M3 16h6"/></svg>Integration</div>
    <div class="skill" style="left:211px;top:222px"><svg width="22" height="22" viewBox="0 0 22 22" fill="none" stroke="#fff" stroke-width=".8"><path d="M3 10h4v10H3zM7 11l4-8c2 0 2 2 2 4h5c1 0 2 1 1.5 2.5L18 18c-.3 1-1 2-2 2H7"/></svg>Testledning</div>
    <div class="skill" style="left:295px;top:222px"><svg width="22" height="22" viewBox="0 0 22 22" fill="none" stroke="#fff" stroke-width=".8"><rect x="3" y="3" width="14" height="12"/><path d="M5 12l3-3 3 2 4-5"/><circle cx="16" cy="16" r="4"/></svg>Affärskritisk drift</div>
    <div class="skill" style="left:375px;top:222px"><svg width="22" height="22" viewBox="0 0 22 22" fill="none" stroke="#fff" stroke-width=".8"><path d="M11 2l8 3v6c0 5-4 8-8 9-4-1-8-4-8-9V5z"/><path d="M7.5 11l2.5 2.5 4.5-4.5"/></svg>Säkerhet</div>
  </section>

  <!-- Contact form -->
  <p class="side-label" style="left:68px;top:1032px">Kontakta oss idag</p>
  <h2 class="sec-title" style="left:91px;top:952px"><span class="indent">Söker</span><span class="line">Ni Kompetens?</span></h2>
  <p class="form-label" style="left:91px;top:1006px;color:var(--muted)">Fyll i formuläret så återkommer vi inom kort.</p>
  <p class="form-label" style="left:251px;top:1006px">Namn*</p>
  <p class="form-label" style="left:351px;top:1006px">Företag*</p>
  <div class="field" style="left:251px;top:1017px"></div>
  <div class="field" style="left:351px;top:1017px"></div>
  <p class="form-label" style="left:251px;top:1044px">E-post*</p>
  <p class="form-label" style="left:351px;top:1044px">Telefonnummer*</p>
  <div class="field" style="left:251px;top:1055px"></div>
  <div class="field" style="left:351px;top:1055px"></div>
  <p class="form-label" style="left:251px;top:1081px">Ort*</p>
  <p class="form-label" style="left:351px;top:1081px">Vilken hjälp behöver du?</p>
  <div class="field" style="left:251px;top:1092px"></div>
  <div class="field" style="left:351px;top:1092px"></div>
  <a class="send">SKICKA</a>

  <!-- Partners -->
  <section class="partners">
    <p class="side-label" style="left:55px;top:120px">Våra partners</p>
    <h2 class="sec-title" style="left:78px;top:36px"><span class="indent">Ural Av</span><span class="line">Våra Ramavtal</span></h2>
    <div class="badge" style="left:78px;top:93px"></div>
    <div class="badge" style="left:174px;top:93px"></div>
    <div class="badge" style="left:270px;top:93px"></div>
    <div class="badge" style="left:366px;top:93px"></div>
    <div class="badge" style="left:78px;top:117px"></div>
    <div class="badge" style="left:174px;top:117px"></div>
    <div class="badge" style="left:270px;top:117px"></div>
    <div class="badge" style="left:366px;top:117px"></div>
    <div class="badge" style="left:78px;top:142px"></div>
    <div class="badge" style="left:174px;top:142px"></div>
    <div class="badge" style="left:270px;top:142px"></div>
    <div class="badge" style="left:366px;top:142px"></div>
  </section>

  <!-- Testimonial -->
  <svg style="left:115px;top:1420px" width="22" height="19" viewBox="0 0 22 19" fill="none" stroke="var(--purple)" stroke-width=".7"><path d="M9 2C4 4 1 8 1 13a4 4 0 108 0 4 4 0 00-5-4c1-3 3-5 5-6zM21 2c-5 2-8 6-8 11a4 4 0 108 0 4 4 0 00-5-4c1-3 3-5 5-6z"/></svg>
  <p class="quote-text">Som ett komplement till våra egna avtal har vi valt att samarbeta med Tarnholm. Tarnholm hjälper oss att hitta uppdrag där vi har full insyn i pris och marginaler. Vi får professionellt stöd genom hela processen och kan själva utvärdera när och om uppdragen passar våra konsulter.</p>
  <p class="quote-author">– Mats Holmgren, VD, Kvarnhem AB</p>

  <!-- Assignments -->
  <section class="jobs">
    <p class="side-label" style="left:57px;top:108px">Uppdrifter</p>
    <h2 class="sec-title" style="left:77px;top:41px"><span class="indent">Aktuella</span><span class="line">Uppdrag</span></h2>
  </section>
  <div class="job" style="top:1558px"><p class="job-title">Interimschef</p><p class="job-place">PLACERINGSORT: GÖTEBORG / VARBERG</p><svg class="job-arrow" width="7" height="5" viewBox="0 0 7 5"><path d="M0 2.5h6M4 .5l2 2-2 2" fill="none" stroke="#555" stroke-width=".4"/></svg></div>
  <div class="job" style="top:1584px"><p class="job-title" style="color:var(--purple)">Kontinuerligt underhåll och drift</p><p class="job-place">PLACERINGSORT: KARLSKRONA</p><svg class="job-arrow" width="7" height="5" viewBox="0 0 7 5"><path d="M0 2.5h6M4 .5l2 2-2 2" fill="none" stroke="#555" stroke-width=".4"/></svg></div>
  <div class="job" style="top:1610px"><p class="job-title">Senior Embedded Firmware Engineer</p><p class="job-place">PLACERINGSORT: STOCKHOLM</p><svg class="job-arrow" width="7" height="5" viewBox="0 0 7 5"><path d="M0 2.5h6M4 .5l2 2-2 2" fill="none" stroke="#555" stroke-width=".4"/></svg></div>
  <div class="job" style="top:1636px"><p class="job-title">PLM Administrator</p><p class="job-place">PLACERINGSORT: MÖLNDAL</p><svg class="job-arrow" width="7" height="5" viewBox="0 0 7 5"><path d="M0 2.5h6M4 .5l2 2-2 2" fill="none" stroke="#555" stroke-width=".4"/></svg></div>
  <div class="jobs-photo" role="img" aria-label="Photo of two colleagues reviewing a notebook in a bright office"></div>
  <a class="register">REGISTRERA PROFIL</a>

  <!-- Team -->
  <p class="side-label" style="left:68px;top:1862px">Gruppmedlemmar</p>
  <h2 class="sec-title" style="left:91px;top:1792px"><span class="line" style="padding-left:23px">Vi På</span><span class="line">Tarnholm</span></h2>
  <div class="person" style="left:91px;top:1849px">
    <div class="avatar" role="img" aria-label="Portrait photo of team member"><div class="fill"></div></div>
    <p class="person-name">Elin Varga</p><p class="person-role">Leverans- och Partneransvarig</p><p class="person-link">in</p>
  </div>
  <div class="person active" style="left:219px;top:1859px">
    <div class="avatar" role="img" aria-label="Portrait photo of team member"><div class="fill"></div></div>
    <p class="person-name">Sara Lindqvist</p><p class="person-role">Leverans- och Partneransvarig</p><p class="person-link">in</p>
  </div>
  <div class="person" style="left:348px;top:1869px">
    <div class="avatar" role="img" aria-label="Portrait photo of team member"><div class="fill"></div></div>
    <p class="person-name">Johanna Ek</p><p class="person-role">Leveranskoordinator</p><p class="person-link">in</p>
  </div>

  <!-- News -->
  <section class="news">
    <p class="side-label" style="left:55px;top:102px">Leverantör</p>
    <h2 class="sec-title" style="left:78px;top:38px"><span class="line">Nyheter</span></h2>
  </section>
  <div class="news-item" style="top:2103px"><p>Utökat samarbete med Norrvik Fordon</p><svg width="6" height="4" viewBox="0 0 6 4"><path d="M0 2h5M3.5.5L5 2 3.5 3.5" fill="none" stroke="var(--purple)" stroke-width=".4"/></svg></div>
  <div class="news-item" style="top:2135px"><p>Vi utökar vår spetskompetens, nu även inom Ekonomi och HR</p><svg width="6" height="4" viewBox="0 0 6 4"><path d="M0 2h5M3.5.5L5 2 3.5 3.5" fill="none" stroke="var(--purple)" stroke-width=".4"/></svg></div>
  <div class="news-item" style="top:2166px;border-bottom:none"><p>MSP</p><svg width="6" height="4" viewBox="0 0 6 4"><path d="M0 2h5M3.5.5L5 2 3.5 3.5" fill="none" stroke="var(--purple)" stroke-width=".4"/></svg></div>

  <!-- Footer -->
  <p class="footer-item" style="left:69px;font-size:2.6px">© Tarnholm 2020 · Tarnholm is part of Kvarnhem AB</p>
  <p class="footer-item" style="left:181px"><svg width="5" height="6" viewBox="0 0 5 6"><path d="M2.5 5.8S.3 3.5.3 2.2a2.2 2.2 0 014.4 0C4.7 3.5 2.5 5.8 2.5 5.8z" fill="none" stroke="var(--purple)" stroke-width=".4"/></svg>Ekbacksgatan 12, 116 45 Stockholm</p>
  <p class="footer-item" style="left:304px"><svg width="6" height="6" viewBox="0 0 6 6"><path d="M1 .5l1.2 1.3-.6.9c.5 1 1 1.5 1.8 1.9l.9-.6L5.5 5c-.5.6-1 .8-1.6.6C2.3 5 1 3.7.4 2.1.3 1.5.5 1 1 .5z" fill="none" stroke="var(--purple)" stroke-width=".4"/></svg>+46 (0) 8-555 010 20</p>
  <p class="footer-item" style="left:398px"><svg width="6" height="5" viewBox="0 0 6 5"><rect x=".3" y=".5" width="5.4" height="4" fill="none" stroke="var(--purple)" stroke-width=".4"/><path d="M.3.5L3 2.8 5.7.5" fill="none" stroke="var(--purple)" stroke-width=".4"/></svg>info@tarnholm.se</p>
</main>
</body>
</html>
```